Stage Design Company Business Card

We are looking to step up up our business card design for our team.

We are a Full service Design and Consultation company for Stage and TV with an emphasis in Theatrical Lighting.

We like our materials to be clean and modern with solid colors free of patterns and gradients. Our brand consists of 4 primary colors Purple, Black, Grey, and White. Provided is our Word Mark as well as our Symbol Logo.

We would like our cards to leave an impression beyond the information, show our attention to design and detail, and make our marks an easily recognized feature (together or apart) for our clients.

We need a warm approachable comfortable feel for some clients, and a professional flair for the board member type clients.

Attached are our brand elements, and our existing cards to give a sense of our style and a glipse at the information we provide on our cards.

Target Market(s)

broad client base from church leaders to high school teachers and architects.

Industry/Entity Type

Business

Contact Information for Business Card

We format our phone number with periods not parenthesis or dashes. Information will be edited for each of our team members, and team member specific cards are not part of this scope, but rather a template so to speak.

Font styles to use
Sans Serif

Colors
6b449b
ffffff
000000
333333
aaaaaa

Requirements
Must have
• Wordmark and logo mark present (does not need to exist on the same side of card)
• Brand Colors,
• Name, Phone, Email, Address.
• Unique choices that make someone stop and take a second look
Nice to have
• It would be nice to somehow convey what we DO, as our brand name does not lend itself to this, outside of an obvious tagline though.....
• social media if not crowded. all of our handles match (instagram, twitter, facebook)
Should not have
• "clipart"

```html
<!DOCTYPE html>
<html lang="en">
<head>
<meta charset="utf-8">
<title>Marlow Staging – Business Card</title>
<link rel="stylesheet" href="https://fonts.googleapis.com/css2?family=Open+Sans:wght@400;600;700&display=swap">
<style>
  :root {
    --backdrop: #d9d9dc;
    --brand-purple: #3b2670;
    --ink: #111111;
    --paper: #ffffff;
    --mist: #e6e4ee;
    --soft-white: #e9e6f3;
  }
  * { box-sizing: border-box; margin: 0; padding: 0; }
  html, body { width: 1200px; height: 900px; overflow: hidden; }
  body {
    background: var(--backdrop);
    font-family: "Open Sans", Arial, sans-serif;
    position: relative;
  }
  .card {
    position: absolute;
    width: 700px;
    height: 400px;
    overflow: hidden;
    box-shadow: 0 10px 28px rgba(0,0,0,.22);
  }
  /* Front */
  .card--front {
    left: 440px; top: 40px;
    background: var(--brand-purple);
    color: var(--soft-white);
  }
  .front-lockup {
    position: absolute;
    left: 150px; top: 130px;
    display: flex; align-items: center; gap: 28px;
  }
  .brand-dot {
    width: 74px; height: 74px; border-radius: 50%;
    background: var(--soft-white);
    flex: none;
  }
  .front-name {
    font-size: 52px; font-weight: 700; letter-spacing: 22px; line-height: 1;
  }
  .front-sub {
    margin-top: 14px;
    font-size: 13px; font-weight: 400; letter-spacing: 15px;
  }
  .front-web {
    margin-top: 12px;
    font-size: 20px; font-weight: 400; letter-spacing: 8px;
  }
  /* Back */
  .card--back {
    left: 60px; top: 470px;
    background: var(--paper);
    color: var(--ink);
  }
  .back-decor {
    position: absolute; right: -110px; bottom: -150px;
    width: 440px; height: 440px; border-radius: 50%;
    background: var(--mist);
  }
  .wordmark {
    position: absolute; left: 48px; top: 44px;
    color: var(--brand-purple);
  }
  .wordmark-name {
    font-size: 44px; font-weight: 700; letter-spacing: 26px; line-height: 1;
  }
  .wordmark-sub {
    margin-top: 14px;
    font-size: 12px; letter-spacing: 17px;
  }
  .contact {
    position: absolute; left: 48px; bottom: 56px;
    display: flex; align-items: center; gap: 22px;
  }
  .person-name {
    font-size: 21px; font-weight: 700; letter-spacing: 5px;
  }
  .person-address {
    margin-top: 6px; font-size: 15px; letter-spacing: 1.5px;
  }
  .divider { width: 1.5px; height: 58px; background: var(--ink); }
  .contact-lines { list-style: none; }
  .contact-lines li {
    display: flex; align-items: center; gap: 10px;
    font-size: 17px; letter-spacing: 1.5px; line-height: 1.7;
  }
  .contact-icon { width: 20px; height: 20px; flex: none; }
</style>
</head>
<body>

<section class="card card--front" aria-label="Card front">
  <div class="front-lockup">
    <span class="brand-dot" aria-hidden="true"></span>
    <div>
      <div class="front-name">MARLOW</div>
      <div class="front-sub">STAGING</div>
      <div class="front-web">MARLOW-S.COM</div>
    </div>
  </div>
</section>

<section class="card card--back" aria-label="Card back">
  <span class="back-decor" aria-hidden="true"></span>
  <div class="wordmark">
    <div class="wordmark-name">MARLOW</div>
    <div class="wordmark-sub">STAGING</div>
  </div>
  <div class="contact">
    <div class="person">
      <div class="person-name">EVAN R MARLOW</div>
      <div class="person-address">52 N ELM ST, TEMPE, AZ 85281</div>
    </div>
    <span class="divider" aria-hidden="true"></span>
    <ul class="contact-lines">
      <li>
        <svg class="contact-icon" viewBox="0 0 20 20" aria-hidden="true">
          <rect width="20" height="20" fill="#3b2670"/>
          <path d="M5 6c0-1 1-2 2-2h6c1 0 2 1 2 2v1h-3V6H8v1H5zM6 9h8l1 6H5z" fill="#fff"/>
        </svg>
        480.555.0147
      </li>
      <li>
        <svg class="contact-icon" viewBox="0 0 20 20" aria-hidden="true">
          <rect width="20" height="20" fill="#3b2670"/>
          <rect x="4" y="6" width="12" height="8" fill="none" stroke="#fff" stroke-width="1.4"/>
          <path d="M4 6l6 5 6-5" fill="none" stroke="#fff" stroke-width="1.4"/>
        </svg>
        EVAN@MARLOW-S.COM
      </li>
    </ul>
  </div>
</section>

</body>
</html>
```